Riverline Estate Holdings Co.

We need a logo and business card design for a Hong Kong based real estate company, KDT Land. We are want the brand to reflect the owners forward thinking, creative, and trend setting projects, while also reflecting a sense of security and strength. We invest in industrial properties which we convert to co-living or co-working spaces. KDT stands for Greater Bay Area which is the region around southern China including HK, Macau, and 9 other Chinese cities...made up of approx. 68 million people. There are massive infrastructure projects including the bridge to Macau and high-speed rail to SZ and the bridge connecting SZ and Zhongshan.

Target Market(s)

Chinese and western retail investors, as well as institutional investors

Industry/Entity Type

Real Estate Development

Contact Information for Business Card

Owen Tallis
CEO
owen@kdtland-hq.com
M + 852 9416 2057
F + 852 3582 0400
Suite 2207, The Meridale, 41 Larchmont Rd., Central, Hong Kong

Logo Text

kdt land (company name) lifestyle property development (underneath)

Colors

Designer to choose colors to be used in the design.

Requirements
Must have
• Details listed above. One side should include the logo and company name...kdt land in modern, hip styling with "lifestyle property development"
Nice to have
• Could be a Black card, with metallic purple "kdt" and white "land"...but open great design ideas
Should not have
• boring and traditional layout

```html
<!DOCTYPE html>
<html lang="en">
<head>
<meta charset="utf-8">
<title>KDT Land – Business Card</title>
<link rel="stylesheet" href="https://fonts.googleapis.com/css2?family=Montserrat:wght@500&family=Oswald:wght@500&family=Work+Sans:wght@400&display=swap">
<style>
  :root {
    --backdrop: #2a2a2c;
    --card: #1c1c1e;
    --purple: #6a36a8;
    --purple-light: #7b44c0;
    --white: #f2f2f2;
  }
  * { margin: 0; padding: 0; box-sizing: border-box; }
  html, body { width: 1200px; height: 900px; overflow: hidden; }
  body {
    background: var(--backdrop);
    display: flex;
    flex-direction: column;
    align-items: center;
    justify-content: center;
    gap: 50px;
  }
  .card {
    position: relative;
    width: 630px;
    height: 360px;
    background: var(--card);
    border-bottom: 6px solid var(--purple);
    box-shadow: 0 10px 24px rgba(0,0,0,0.45);
  }
  /* Front */
  .brand {
    position: absolute;
    left: 70px;
    top: 110px;
  }
  .brand-row {
    display: flex;
    align-items: center;
    gap: 18px;
  }
  .brand-mark {
    width: 22px;
    height: 22px;
    background: var(--purple-light);
    flex: none;
  }
  .brand-name {
    font-family: "Work Sans", sans-serif;
    font-weight: 400;
    font-size: 54px;
    color: var(--white);
    line-height: 1;
  }
  .brand-tagline {
    font-family: "Work Sans", sans-serif;
    font-weight: 400;
    font-size: 15px;
    letter-spacing: 3px;
    text-transform: lowercase;
    color: var(--purple-light);
    margin-top: 14px;
    margin-left: 40px;
  }
  /* Back */
  .person {
    position: absolute;
    right: 350px;
    top: 124px;
    text-align: right;
  }
  .person-name {
    font-family: "Oswald", sans-serif;
    font-weight: 500;
    font-size: 36px;
    letter-spacing: 1px;
    color: var(--purple-light);
    line-height: 1.1;
  }
  .person-role {
    font-family: "Montserrat", sans-serif;
    font-weight: 500;
    font-size: 15px;
    color: var(--white);
    margin-top: 2px;
  }
  .divider {
    position: absolute;
    left: 300px;
    top: 126px;
    width: 2px;
    height: 64px;
    background: var(--white);
  }
  .contacts {
    position: absolute;
    left: 326px;
    top: 122px;
    list-style: none;
    font-family: "Work Sans", sans-serif;
    font-size: 17px;
    color: var(--white);
    line-height: 24px;
  }
  .contacts li { display: flex; align-items: center; gap: 14px; }
  .contacts svg { width: 11px; height: 11px; fill: var(--purple-light); flex: none; }
  .address {
    position: absolute;
    left: 50px;
    bottom: 50px;
    font-family: "Work Sans", sans-serif;
    font-size: 17px;
    color: var(--white);
  }
</style>
</head>
<body>
  <section class="card card-front">
    <div class="brand">
      <div class="brand-row">
        <span class="brand-mark" aria-hidden="true"></span>
        <span class="brand-name">KDT Land</span>
      </div>
      <div class="brand-tagline">lifestyle property development</div>
    </div>
  </section>

  <section class="card card-back">
    <div class="person">
      <div class="person-name">OWEN TALLIS</div>
      <div class="person-role">CEO</div>
    </div>
    <div class="divider"></div>
    <ul class="contacts">
      <li>
        <svg viewBox="0 0 12 12" aria-hidden="true"><path d="M2.5 0.5l2 2.3-1 1.3c.7 1.5 1.9 2.7 3.4 3.4l1.3-1 2.3 2-1.1 2c-4.6-.3-8.3-4-8.6-8.6z"/></svg>
        + 852 9416 2057
      </li>
      <li>
        <svg viewBox="0 0 12 12" aria-hidden="true"><rect x="3" y="0.5" width="6" height="3"/><rect x="0.5" y="4" width="11" height="5" rx="1"/><rect x="3" y="8" width="6" height="3.5"/></svg>
        + 852 3582 0400
      </li>
      <li>
        <svg viewBox="0 0 12 12" aria-hidden="true"><path d="M0.5 2.5h11v7h-11z" fill="none" stroke="#7b44c0" stroke-width="1.2"/><path d="M0.5 2.5l5.5 4 5.5-4" fill="none" stroke="#7b44c0" stroke-width="1.2"/></svg>
        owen@kdtland-hq.com
      </li>
    </ul>
    <p class="address">Suite 2207, The Meridale, 41 Larchmont Rd., Central, Hong Kong</p>
  </section>
</body>
</html>
```